Varemo Group Business Card Design

The CEO is looking for a new trendy look for his business card.
You can stay with current branding or come up with something new/creative. It can be 3D, including Medical Office buildings. You can use our logo in a variety of colors. Please include name, title, company name, company website, email address, cell number

Target Market(s)

Real Estate Development and Construction

Industry/Entity Type

Health care real estate

Contact Information for Business Card

Rohesh Kumbar, CEO M-727.418.9062 E-roheshkumbar@varemo.com Address:4100 Lindell Ave, Tampa, FL 33611 www.varemo.com

Font styles to use
Other font styles liked:
• Be creative

Requirements
Must have
• Creative, trendy look
Nice to have
• Please go to our website to get a feel- www. varemo.com
Should not have
• small fonts

```html
<!DOCTYPE html>
<html lang="en">
<head>
<meta charset="utf-8">
<title>Varemo Group – Business Card</title>
<link rel="stylesheet" href="https://fonts.googleapis.com/css2?family=Arimo:wght@400;700&family=Lato:wght@400;700&display=swap">
<style>
  :root {
    --stage-light: #3b3b3b;
    --stage-dark: #161616;
    --brand-red: #d0232d;
    --brand-red-deep: #b21c25;
    --name-red: #ad1f24;
    --navy: #1e2a4a;
    --ink: #1c1c1c;
    --white: #ffffff;
    --tower-blue: #2c63c4;
    --tower-sky: #7cc3ef;
    --tower-pale: #eef4fb;
    --sketch-grey: #f1f1f1;
  }
  * { margin: 0; padding: 0; box-sizing: border-box; }
  html, body { width: 1200px; height: 1000px; overflow: hidden; }
  body {
    position: relative;
    background: radial-gradient(ellipse at 50% 45%, var(--stage-light) 0%, var(--stage-dark) 80%);
    font-family: "Lato", Arial, sans-serif;
  }
  .card {
    position: absolute;
    left: 203px;
    width: 794px;
    height: 454px;
    border-radius: 28px;
    overflow: hidden;
  }
  .card--front {
    top: 35px;
    background: radial-gradient(circle at 45% 35%, var(--brand-red) 0%, var(--brand-red-deep) 85%);
  }
  .card--back { top: 511px; background: var(--white); }

  .tower-art {
    position: absolute;
    left: 492px; top: 0;
    width: 302px; height: 100%;
    background: linear-gradient(90deg, var(--tower-blue) 0%, var(--tower-pale) 18%, var(--tower-pale) 30%, var(--tower-sky) 45%, var(--tower-pale) 62%, var(--tower-pale) 80%, var(--tower-blue) 90%, var(--tower-sky) 100%);
  }
  .wordmark {
    position: absolute;
    font-family: "Arimo", Arial, sans-serif;
    font-weight: 700;
    line-height: 1;
    text-align: right;
  }
  .wordmark__main { display: block; letter-spacing: -2px; }
  .wordmark__sub { display: block; }
  .card--front .wordmark { left: 130px; top: 182px; color: var(--white); }
  .card--front .wordmark__main { font-size: 66px; }
  .card--front .wordmark__sub { font-size: 28px; margin-top: 2px; }

  .sketch-art {
    position: absolute;
    left: 0; top: 0;
    width: 338px; height: 100%;
    background: linear-gradient(90deg, var(--sketch-grey), #fafafa 60%, var(--white));
  }
  .holder { position: absolute; left: 381px; top: 76px; }
  .holder__name {
    font-family: "Arimo", Arial, sans-serif;
    font-weight: 700;
    font-size: 34px;
    color: var(--name-red);
    letter-spacing: 0.5px;
    line-height: 1;
  }
  .holder__title {
    font-family: "Arimo", Arial, sans-serif;
    font-weight: 700;
    font-size: 19px;
    color: var(--navy);
    margin-top: 9px;
  }
  .contacts { position: absolute; left: 381px; top: 163px; list-style: none; }
  .contacts li {
    display: flex;
    align-items: flex-start;
    font-size: 20px;
    color: var(--ink);
    line-height: 25px;
    margin-bottom: 7px;
  }
  .contacts svg { width: 20px; height: 22px; margin-right: 10px; flex: none; fill: var(--navy); }
  .card--back .wordmark { right: 32px; bottom: 30px; color: var(--name-red); }
  .card--back .wordmark__main { font-size: 62px; }
  .card--back .wordmark__sub { font-size: 27px; margin-top: 2px; }
</style>
</head>
<body>
  <section class="card card--front">
    <div class="wordmark">
      <span class="wordmark__main">Varemo</span>
      <span class="wordmark__sub">group</span>
    </div>
    <div class="tower-art" role="img" aria-label="Illustration of a blue and white medical office tower"></div>
  </section>

  <section class="card card--back">
    <div class="sketch-art" role="img" aria-label="Faint line drawing of an office tower facade"></div>
    <div class="holder">
      <h1 class="holder__name">ROHESH KUMBAR</h1>
      <p class="holder__title">CEO</p>
    </div>
    <ul class="contacts">
      <li>
        <svg viewBox="0 0 20 22"><path d="M5 1h10a2 2 0 0 1 2 2v16a2 2 0 0 1-2 2H5a2 2 0 0 1-2-2V3a2 2 0 0 1 2-2zm0 2v16h10V3zm4 13h2v2H9z"/></svg>
        M-727.418.9062
      </li>
      <li>
        <svg viewBox="0 0 20 22"><path d="M19 3 1 11l6 2 2 6 3-4 4 3z"/></svg>
        roheshkumbar@varemo.com
      </li>
      <li>
        <svg viewBox="0 0 20 22"><path d="M10 2a9 9 0 1 0 0 18 9 9 0 0 0 0-18zm0 2c1 1.4 1.7 3.2 1.9 5H8.1C8.3 7.2 9 5.4 10 4zm-2 .4A11 11 0 0 0 6.1 9H3.3A7 7 0 0 1 8 4.4zM3.3 13h2.8A11 11 0 0 0 8 17.6 7 7 0 0 1 3.3 13zM8.1 13h3.8c-.2 1.8-.9 3.6-1.9 5-1-1.4-1.7-3.2-1.9-5zM12 17.6A11 11 0 0 0 13.9 13h2.8a7 7 0 0 1-4.7 4.6zM13.9 9A11 11 0 0 0 12 4.4 7 7 0 0 1 16.7 9zM3 11h14v0z"/></svg>
        www.varemo.com
      </li>
      <li>
        <svg viewBox="0 0 20 22"><path d="M10 1a7 7 0 0 0-7 7c0 5 7 13 7 13s7-8 7-13a7 7 0 0 0-7-7zm0 10a3 3 0 1 1 0-6 3 3 0 0 1 0 6z"/></svg>
        <span>4100 Lindell Ave, Tampa,<br>FL 33611</span>
      </li>
    </ul>
    <div class="wordmark">
      <span class="wordmark__main">Varemo</span>
      <span class="wordmark__sub">group</span>
    </div>
  </section>
</body>
</html>
```